Fabulous Flyer for dream outdoor living construction and design company

we want a flyer designed to hand out at a large home show. We are a backyard dream design and build out company. come to us with or without your plans and we will build it for you. What makes us unique is that we have a 21,000 square foot showroom with lots of fountains, outdoor kitchens, grills, paver showroom, yard art, rock and much more for you to see, feel and buy amazing stuff... we carry 100's of top brand products like stonevane, tallowmere, gray hollis and emberlux products. we build pergolas, outdoor kitchens, firepits, fireplaces, water features and more. our 3-d designs help you live it before you build it. but design is not our main function, construction is. sunvalemossyard.example has a 3-d video on home page so you can see what we can do. Question...What do we put in a flyer that will invite people to our showroom, offer them free estimates, stress that we want to be chosen to do the build out, reqardless who designed it and most importantly that they are important to us. We are honored to be invited into their home to build their dream back yard. we do $2000 to $200,000 dreamscapes. How do we say that in a flyer??? How would you say it?

Target Market(s)

home owners wanting to add an outdoor space , new construction who need a back yard put in. People who have $5000 to $100,000 to spend on their yards

Industry/Entity Type

Construction

Requirements
Must have
• lots to say but how do we keep it peaceful and simple
• Every company shows a photo of a back yard they did. lets use food on a grill from Corvettas grill site, a family around a gorgeous firepit or people enjoying life in their dream back yard. How can ours be different. we are not a pick up truck contractor. we have an amazing store showroom, craftsman to do the work and top brand name products and 30 year experienced designers. message we design and build. free estimates come see our store outdoor kitchens, pergolas, pavers, stone and more....
Nice to have
• professional look. we are an earth conscious company who cares about our planet, our customers and honors our people. i added a photo of one of our guys making a leaf inside a paver patio. i think it shows we are an artful paver construction company and showcases one of our craftsman.
Should not have
• i only posted a few photos but i think they are important. so words with no photos not so good. photos are available on web sites of our product manufacturer as well.

```html
<!DOCTYPE html>
<html lang="en">
<head>
<meta charset="utf-8">
<title>Sunvale Mossyard – Dream Backyard Flyer</title>
<link href="https://fonts.googleapis.com/css2?family=Oswald:wght@500;600;700&family=Archivo+Black&family=Arimo:wght@400&display=swap" rel="stylesheet">
<style>
  :root {
    --cream: #f0efdf;
    --olive: #737833;
    --olive-dark: #6a7032;
    --lime: #bcbc32;
    --sage: #a9aa6c;
    --rust: #8a4520;
    --white: #ffffff;
    --photo-stone: #8b9487;
    --photo-garden: #7e9c63;
    --photo-fountain: #8f7a5c;
  }
  * { box-sizing: border-box; margin: 0; padding: 0; }
  html, body { width: 927px; height: 1200px; overflow: hidden; background: var(--white); }
  .flyer { position: relative; width: 927px; height: 1200px; overflow: hidden; background: var(--white); }

  .header-wave { position: absolute; left: 0; top: 0; width: 927px; height: 300px; }

  .brand-mark {
    position: absolute; left: 92px; top: 36px; width: 152px; height: 152px;
    border-radius: 50%; background: var(--olive);
  }
  .brand-name {
    position: absolute; left: 264px; top: 44px;
    font-family: "Archivo Black", sans-serif; font-weight: 400; font-size: 60px; line-height: 56px;
    color: var(--olive-dark); letter-spacing: 1px;
  }
  .brand-tagline {
    position: absolute; left: 262px; top: 156px;
    font-family: "Oswald", sans-serif; font-weight: 600; font-size: 27px; line-height: 34px;
    color: var(--sage); letter-spacing: 0.5px; white-space: nowrap;
  }

  .headline { position: absolute; left: 96px; top: 272px; width: 306px; text-align: center; font-weight: 400; }
  .headline-lead, .headline-tail {
    font-family: "Archivo Black", sans-serif; font-weight: 400; font-size: 40px; color: var(--olive); line-height: 1;
  }
  .headline-main {
    font-family: "Oswald", sans-serif; font-weight: 700; font-size: 74px; line-height: 88px;
    color: var(--lime); margin: 26px 0 22px;
  }

  .benefits {
    position: absolute; left: 472px; top: 300px; width: 430px; list-style: none; text-align: center;
    font-family: "Arimo", sans-serif; font-size: 24px; line-height: 31px; letter-spacing: 0.8px; color: var(--olive);
  }
  .benefits li { margin-bottom: 31px; }

  .divider-band { position: absolute; left: 0; top: 767px; width: 927px; height: 15px; background: var(--rust); }

  .estimate-badge {
    position: absolute; left: 138px; top: 617px; width: 292px; height: 186px;
    border-radius: 50%; background: var(--rust); transform: rotate(-6deg);
    display: flex; flex-direction: column; align-items: center; justify-content: center;
    font-family: "Oswald", sans-serif; color: var(--white); text-align: center;
  }
  .estimate-badge .small { font-size: 22px; font-weight: 600; line-height: 1.05; }
  .estimate-badge .big { font-size: 60px; font-weight: 700; line-height: 1; letter-spacing: 3px; }
  .estimate-badge .mid { font-size: 46px; font-weight: 700; line-height: 1; }

  .photo { position: absolute; top: 804px; height: 324px; }
  .photo-sculptures { left: 26px; width: 255px; background: linear-gradient(160deg, #b2b39a, var(--photo-stone) 55%, #5f6a55); }
  .photo-pergola { left: 296px; width: 333px; background: linear-gradient(180deg, #cfe2f2 0%, #a8cbe3 30%, #a3825a 45%, var(--photo-garden) 70%, #5c8a3c); }
  .photo-fountain { left: 646px; width: 254px; background: linear-gradient(170deg, #4f6b3c, var(--photo-fountain) 55%, #9a9a92); }

  .web-address {
    position: absolute; left: 0; top: 1142px; width: 927px; text-align: center;
    font-family: "Arimo", sans-serif; font-size: 34px; line-height: 40px; color: var(--olive);
  }
</style>
</head>
<body>
<main class="flyer">
  <svg class="header-wave" viewBox="0 0 927 300" aria-hidden="true">
    <path d="M0 0 H927 V240 C780 220 620 198 470 212 C310 228 170 290 0 290 Z" fill="var(--cream)"/>
  </svg>

  <div class="brand-mark" aria-hidden="true"></div>
  <div class="brand-name">SUNVALE<br>MOSSYARD</div>
  <div class="brand-tagline">YOUR FIREPLACE AND OUTDOOR LIVING COMPANY</div>

  <h1 class="headline">
    <div class="headline-lead">Make your</div>
    <div class="headline-main">DREAM<br>BACKYARD</div>
    <div class="headline-tail">a reality!</div>
  </h1>

  <ul class="benefits">
    <li>- Our 3-D designs help you<br>“live it” before you build it</li>
    <li>- We carry top brands like<br>Stonevane, Tallowmere, Gray<br>Hollis, and Emberlux</li>
    <li>- We build pergolas, outdoor<br>kitchens, firepits, fireplaces,<br>water features, and more</li>
    <li>- We create dreamscapes<br>at all budgets - from<br>$2,000 to $200,000</li>
  </ul>

  <div class="divider-band"></div>

  <div class="estimate-badge">
    <span class="small">COME BY FOR A</span>
    <span class="big">FREE</span>
    <span class="mid">ESTIMATE!</span>
  </div>

  <div class="photo photo-sculptures" role="img" aria-label="Photo of large stone head garden sculptures among shrubs"></div>
  <div class="photo photo-pergola" role="img" aria-label="Photo of a wooden pergola over a stone fountain wall with flower beds"></div>
  <div class="photo photo-fountain" role="img" aria-label="Photo of a tiered stone spill fountain in a round basin beside potted plants"></div>

  <div class="web-address">sunvalemossyard.example</div>
</main>
</body>
</html>
```